Consultant company (start up) needs a bold, yet simple web design

We need a we design for "K7P Ledger & Consulting". As our name implies we are a consultant firm helping companies with public sector business (tenders), but also helping the buyer side. We provide market research and reports, advice (legal and business) and hands-on-help with tender applications (projectleader; analysing critiera and texts, document reviews, etc). We have a rather uniqe position in our market with our mixed competences of branding and market communication, formal management systems, and public tenders.

We have a strong drive to make tender business simple for our clients: we will take care of the complicated!

We want our web design to be bold, yet clean and simple, communicating:

Competence; Commitment, Simplicity (for the customer).
Updates

Reason: For different reasons our web project was put on hold/was delayed a few days. As of today we are kicking life into it again, and expect to come back with feedback on designs in the next days. Best regards, Mattias

Target Market(s)

We primarily help companies aiming for public contracts.

Industry/Entity Type

Business Consultant

Contact Information for Business Card

Company logo; First name, Last name, Titel, webadress; personal e-mail
Maybe: a motto like "Offentliga affärer. Enklare" ("Public business. Made simple.")

Coding

Coded - Design and coding required

Font styles to use
Sans Serif

Colors

Designer to choose colors to be used in the design.

Requirements
Must have
• Dual language (Swedish and English)
• Responsive design, many people will view our webpage on their phone or tavlo.
• We want to make our position clear, stating what distinguishes us from "the rest of the pack" in maybe with on the starting page.
• [Will update brief; need to think this through]
Nice to have
• We have our logo in three colours. Green is our first. We are not yet sure why we have the different colurs. Maybe (just maybe!) the different colours can be put to use?
• We need help with the choice of images.
Should not have
• Never boring.

```html
<!DOCTYPE html>
<html lang="en">
<head>
<meta charset="utf-8">
<title>K7P Ledger &amp; Consulting</title>
<link href="https://fonts.googleapis.com/css2?family=Lato:ital,wght@0,400;0,700;1,400&family=Raleway:wght@400;500;600&display=swap" rel="stylesheet">
<style>
:root{
  --green:#8cbb3c;
  --green-dark:#3f8a2a;
  --ink:#222;
  --body:#555;
  --topbar:#5a5a5a;
  --footer:#333;
  --footer-line:#4a4a4a;
  --soft:#f0f0f0;
  --white:#fff;
}
*{box-sizing:border-box;margin:0;padding:0}
html,body{width:670px;height:1200px;overflow:hidden;background:var(--white)}
body{position:relative;font-family:'Lato',sans-serif;color:var(--body)}
.abs{position:absolute}
.head{font-family:'Raleway',sans-serif;color:var(--ink);font-weight:400}
.head span{color:var(--green)}

/* top bar & header */
.topbar{left:0;top:0;width:670px;height:21px;background:var(--topbar)}
.topbar-info{right:42px;top:5px;font-size:8px;color:#eee;display:flex;gap:8px;align-items:center}
.topbar-info svg{vertical-align:-2px;margin-right:3px}
.lang{width:14px;height:9px;background:linear-gradient(#2a3f8f,#c8283a);display:inline-block}
.header{left:0;top:21px;width:670px;height:51px;background:var(--white)}
.logo-tab{left:92px;top:8px;width:176px;height:60px;background:var(--white);border-radius:8px 8px 0 0}
.brand{display:flex;align-items:center;gap:6px;font-family:'Raleway',sans-serif;font-weight:500;color:var(--green-dark)}
.logo-tab .brand{position:absolute;left:12px;top:22px;font-size:12.5px}
.brand-dot{width:14px;height:14px;border-radius:50%;background:var(--green);flex:none}
.nav{top:42px;font-size:7.5px;color:#333;font-family:'Raleway',sans-serif;font-weight:500}
.nav.active{color:var(--green-dark)}
.nav-sep{top:43px;width:1px;height:7px;background:#ccc}

/* hero */
.hero{left:0;top:72px;width:670px;height:293px;background:radial-gradient(ellipse at 62% 30%,#9fb2c4 0%,#6f879d 35%,#3e5264 75%,#2c3a48 100%)}
.hero-title{left:91px;top:190px;font-family:'Raleway',sans-serif;font-size:14.5px;color:var(--white);font-weight:500}
.hero-sub{left:91px;top:213px;font-size:7.2px;line-height:11px;color:#eef}
.btn{height:18px;border-radius:9px;background:var(--green);color:var(--white);font-size:6.6px;font-weight:700;display:flex;align-items:center;padding-left:7px;gap:5px;font-family:'Lato',sans-serif}
.btn i{width:12px;height:12px;border-radius:50%;background:var(--white);display:flex;align-items:center;justify-content:center}
.btn.dark{background:var(--green-dark)}
.dots{display:flex;gap:4px}
.dots b{width:6px;height:6px;border-radius:50%;border:1px solid var(--white)}
.dots b.on{background:var(--green);border-color:var(--green)}
.dots.grey b{border-color:#888}

/* about */
.about-title{left:90px;top:389px;font-size:15px}
.about-line{left:90px;top:414px;width:308px;height:1px;background:#ddd}
.about-line::before{content:"";position:absolute;left:0;top:-1px;width:26px;height:2px;background:var(--green)}
.about-lead{left:90px;top:427px;width:310px;font-size:6.5px;line-height:11px;font-weight:700;color:var(--ink)}
.about-text{left:90px;top:453px;width:310px;font-size:6.3px;line-height:11.3px}

/* inquiry */
.inquiry{left:438px;top:392px;width:142px;height:150px;background:var(--white);box-shadow:0 2px 6px rgba(0,0,0,.15)}
.inquiry h3{height:26px;background:var(--green);color:var(--white);font-family:'Raleway',sans-serif;font-weight:500;font-size:12px;text-align:center;line-height:26px}
.field{position:absolute;left:8px;width:126px;height:18px;border:1px solid #ddd;font-size:6px;padding:5px 6px;color:#777}
.field em{color:#c33;font-style:normal}

/* services */
.services{left:0;top:576px;width:670px;height:286px;background:var(--soft)}
.sec-title{width:670px;text-align:center;font-size:15px}
.sec-line{left:258px;width:154px;height:1px;background:#ccc}
.sec-line::before{content:"";position:absolute;left:64px;top:-1px;width:26px;height:2px;background:var(--green)}
.card{width:155px;height:94px;background:var(--white);border:1px solid #ddd;padding:3px;box-shadow:0 6px 5px -4px rgba(0,0,0,.35)}
.card.on{border-color:var(--green)}
.card div{width:100%;height:100%}
.svc-title{width:155px;text-align:center;font-family:'Raleway',sans-serif;font-size:8.6px;line-height:11px;color:var(--ink)}
.svc-title.on{color:var(--green)}
.svc-text{width:155px;text-align:center;font-size:6.2px;line-height:8.8px}
.plus{width:15px;height:15px;border-radius:50%;background:#999;display:flex;align-items:center;justify-content:center}
.plus.on{background:var(--green)}

/* testimonials */
.avatar{left:170px;top:922px;width:80px;height:80px;border-radius:50%;border:3px solid #eee;background:radial-gradient(circle at 50% 40%,#d8c7b6,#8a8d93 70%,#2e3440)}
.quote{width:36px;height:30px}
.testi-text{left:263px;top:921px;width:234px;font-size:6.4px;line-height:12.3px;font-style:italic}
.testi-name{left:380px;top:982px;width:111px;text-align:right;font-family:'Raleway',sans-serif;font-size:8px;color:var(--green)}
.testi-role{left:380px;top:994px;width:111px;text-align:right;font-size:5.8px;color:#333}

/* footer */
.footer{left:0;top:1030px;width:670px;height:148px;background:var(--footer)}
.foot-h{top:1054px;font-family:'Raleway',sans-serif;font-size:9.6px;color:#eee}
.foot-line{top:1073px;height:1px;background:var(--footer-line)}
.foot-sep{top:1050px;width:1px;height:112px;background:var(--footer-line)}
.foot-link{left:91px;font-size:6.2px;color:#bbb}
.foot-link::before{content:"› ";color:#888}
.foot-link.on{color:var(--green)}
.foot-txt{left:178px;font-size:6.2px;color:#bbb;line-height:9px}
.map{left:322px;top:1082px;width:131px;height:70px;background:linear-gradient(135deg,#d9d4c8,#ece7da 50%,#e6d59a)}
.footer .brand,.foot-brand{color:#bbb}
.social{top:1119px;width:13px;height:13px;border-radius:50%}
.copy{left:0;top:1178px;width:670px;height:22px;background:var(--green);color:var(--white);font-size:6.2px;text-align:center;line-height:22px}
</style>
</head>
<body>

<div class="abs topbar"></div>
<div class="abs topbar-info">
  <span><svg width="8" height="7" viewBox="0 0 8 7"><path d="M0 3 4 0 8 3v4H0z" fill="none" stroke="#eee" stroke-width="1"/></svg>info@k7pconsulting</span>
  <span><svg width="9" height="9" viewBox="0 0 10 10"><circle cx="5" cy="5" r="4.4" fill="none" stroke="#eee" stroke-width=".8"/><path d="M3.3 2.8c0 2 1.6 3.9 3.5 4.3l.5-1-1-.6-.5.5C5 5.5 4.5 5 4.3 4.2l.5-.5-.6-1z" fill="#eee"/></svg>123-555-0190</span>
  <span class="lang" role="img" aria-label="Language selector flag"></span>
  <span>▾</span>
</div>

<header class="abs header"></header>
<div class="abs logo-tab">
  <div class="brand"><span class="brand-dot"></span>K7P Ledger &amp; Consulting</div>
</div>
<nav>
  <span class="abs nav active" style="left:311px">Home</span>
  <span class="abs nav-sep" style="left:357px"></span>
  <span class="abs nav" style="left:380px">About Us</span>
  <span class="abs nav-sep" style="left:437px"></span>
  <span class="abs nav" style="left:460px">Services</span>
  <span class="abs nav-sep" style="left:515px"></span>
  <span class="abs nav" style="left:539px">Contact Us</span>
</nav>

<section>
  <div class="abs hero" role="img" aria-label="Close-up of a hand placing the last piece into a blue jigsaw puzzle"></div>
  <h1 class="abs hero-title">WELCOME TO K7P CONSULTING</h1>
  <p class="abs hero-sub">We Are A Consultant Company That Helps Companies With<br>Public Sector Business But Also Helping The Buyers.</p>
  <div class="abs btn" style="left:90px;top:242px;width:67px">READ MORE <i><svg width="6" height="6" viewBox="0 0 6 6"><path d="M2 1l2 2-2 2" stroke="#3f8a2a" stroke-width="1.2" fill="none"/></svg></i></div>
  <div class="abs dots" style="left:91px;top:269px"><b class="on"></b><b></b><b></b><b></b></div>
</section>

<section>
  <h2 class="abs head about-title">About <span>Us</span></h2>
  <div class="abs about-line"></div>
  <p class="abs about-lead">Nemo enim ipsam voluptatem quia voluptas sit aspernatur aut odit aut fugit, sed quia consequuntur magni dolores eos qui ratione voluptatem</p>
  <p class="abs about-text">Lorem ipsum dolor sit amet, consectetur adipiscing elit, sed do eiusmod tempor incididunt ut labore et dolore magna aliqua. Ut enim ad minim veniam, quis nostrud exercitation ullamco laboris nisi ut aliquip ex ea commodo consequat. Duis aute irure dolor in reprehenderit in voluptate velit esse cillum dolore eu fugiat nulla pariatur. Excepteur sint occaecat cupidatat non proident, sunt in culpa qui officia deserunt mollit anim id est laborumLorem ipsum dolor sit amet, consectetur adipiscing elit, sed do eiusmod tempor incididunt ut labore et dolore magna aliqua.</p>
  <div class="abs btn" style="left:90px;top:533px;width:67px">READ MORE <i><svg width="6" height="6" viewBox="0 0 6 6"><path d="M2 1l2 2-2 2" stroke="#3f8a2a" stroke-width="1.2" fill="none"/></svg></i></div>

  <form class="abs inquiry">
    <h3>Quick Inquiry</h3>
    <div class="field" style="top:36px">Your Name<em>*</em></div>
    <div class="field" style="top:57px">Your Email<em>*</em></div>
    <div class="field" style="top:79px">Your Phone<em>*</em></div>
    <div class="field" style="top:102px;height:30px">Your Message<em>*</em></div>
  </form>
  <div class="abs btn dark" style="left:471px;top:533px;width:76px">SUBMIT FORM <i><svg width="6" height="6" viewBox="0 0 6 6"><path d="M2 1l2 2-2 2" stroke="#3f8a2a" stroke-width="1.2" fill="none"/></svg></i></div>
</section>

<section>
  <div class="abs services"></div>
  <h2 class="abs head sec-title" style="left:0;top:600px">Our <span>Services</span></h2>
  <div class="abs sec-line" style="top:622px"></div>

  <div class="abs card on" style="left:90px;top:636px"><div role="img" aria-label="Hand touching a tablet showing market charts" style="background:linear-gradient(135deg,#cfe0ee,#6f8fb0 60%,#2f4864)"></div></div>
  <div class="abs card" style="left:258px;top:636px"><div role="img" aria-label="Business team meeting around a table" style="background:linear-gradient(135deg,#e8eef2,#6c7a8a 55%,#26303b)"></div></div>
  <div class="abs card" style="left:425px;top:636px"><div role="img" aria-label="Person filling in a document on a blue clipboard" style="background:linear-gradient(135deg,#a5652e,#5a3018 50%,#2a3e7a)"></div></div>

  <h3 class="abs svc-title on" style="left:90px;top:741px">Market Research And<br>Reports</h3>
  <h3 class="abs svc-title" style="left:258px;top:741px">Advice Legal And<br>Business</h3>
  <h3 class="abs svc-title" style="left:425px;top:741px">Hands-on-help With Tender<br>Applications</h3>

  <p class="abs svc-text" style="left:90px;top:769px">Lorem ipsum dolor sit amet, consectetuer adipiscing elit, sed diam nonummy nibh euismod tincidunt ut laoreet dolore.</p>
  <p class="abs svc-text" style="left:258px;top:769px">Lorem ipsum dolor sit amet, consectetuer adipiscing elit, sed diam nonummy nibh euismod tincidunt ut laoreet dolore.</p>
  <p class="abs svc-text" style="left:425px;top:769px">Lorem ipsum dolor sit amet, consectetuer adipiscing elit, sed diam nonummy nibh euismod tincidunt ut laoreet dolore.</p>

  <div class="abs plus on" style="left:160px;top:803px"><svg width="8" height="8" viewBox="0 0 8 8"><path d="M4 1v6M1 4h6" stroke="#fff" stroke-width="1.6"/></svg></div>
  <div class="abs plus" style="left:328px;top:803px"><svg width="8" height="8" viewBox="0 0 8 8"><path d="M4 1v6M1 4h6" stroke="#fff" stroke-width="1.6"/></svg></div>
  <div class="abs plus" style="left:495px;top:803px"><svg width="8" height="8" viewBox="0 0 8 8"><path d="M4 1v6M1 4h6" stroke="#fff" stroke-width="1.6"/></svg></div>
  <div class="abs dots grey" style="left:318px;top:831px"><b class="on"></b><b></b><b></b><b></b></div>
</section>

<section>
  <h2 class="abs head sec-title" style="left:0;top:886px">Clients <span>Testimonials</span></h2>
  <div class="abs sec-line" style="top:908px"></div>

  <svg class="abs" style="left:62px;top:958px" width="14" height="26" viewBox="0 0 14 26"><path d="M12 1 2 13l10 12" fill="none" stroke="#ccc" stroke-width="1.2"/></svg>
  <svg class="abs" style="left:592px;top:958px" width="14" height="26" viewBox="0 0 14 26"><path d="M2 1l10 12L2 25" fill="none" stroke="#ccc" stroke-width="1.2"/></svg>

  <svg class="abs quote" style="left:118px;top:938px" viewBox="0 0 36 30"><path d="M0 8h14v22H0zM0 8C0 2 4 0 10 0v5C6 5 5 7 5 8zM20 8h14v22H20zM20 8c0-6 4-8 10-8v5c-4 0-5 2-5 3z" fill="#ddd"/></svg>
  <svg class="abs quote" style="left:517px;top:938px" viewBox="0 0 36 30"><path d="M2 0h14v22H2zM16 22c0 6-4 8-10 8v-5c4 0 5-2 5-3zM22 0h14v22H22zM36 22c0 6-4 8-10 8v-5c4 0 5-2 5-3z" fill="#ddd"/></svg>

  <div class="abs avatar" role="img" aria-label="Portrait of the client giving the testimonial"></div>
  <p class="abs testi-text">Lorem ipsum dolor sit amet, consectetuer adipiscing elit, sed diam nonummy nibh euismod tincidunt ut laoreet dolore magna aliquam erat volutpat. Ut wisi enim ad minim veniam, quis nostrud exer tation ullamcorper suscipit loboutlaoreet Duissed diam nonummyconsequat. Duissed diam nonummy nibh euismod tincidunt ut laoreet dolore magna .</p>
  <div class="abs testi-name">- Liam Halvorsen</div>
  <div class="abs testi-role">CEO &amp; FOUNDER</div>
</section>

<footer>
  <div class="abs footer"></div>
  <h4 class="abs foot-h" style="left:91px">Quick Links</h4>
  <div class="abs foot-line" style="left:91px;width:58px"></div>
  <span class="abs foot-link on" style="top:1082px">Home</span>
  <span class="abs foot-link" style="top:1099px">About Us</span>
  <span class="abs foot-link" style="top:1117px">Services</span>
  <span class="abs foot-link" style="top:1135px">Contact Us</span>
  <div class="abs foot-sep" style="left:164px"></div>

  <h4 class="abs foot-h" style="left:178px">Contact Detail</h4>
  <div class="abs foot-line" style="left:178px;width:110px"></div>
  <span class="abs foot-txt" style="top:1082px;color:#eee;font-size:6.8px">K7Pconsulting</span>
  <span class="abs foot-txt" style="top:1094px;width:120px">Lorem ipsum dolor sit amet, consecte adipiscing elit,</span>
  <span class="abs foot-txt" style="top:1123px;font-size:8px;color:#ddd"><svg width="8" height="8" viewBox="0 0 10 10" style="vertical-align:-1px;margin-right:5px"><path d="M2 1c0 4 3 8 7 8l1-2-2-1-1 1C5 6 4 5 3 3l1-1-1-2z" fill="#8cbb3c"/></svg>123-555-0190</span>
  <span class="abs foot-txt" style="top:1143px"><svg width="8" height="6" viewBox="0 0 8 6" style="vertical-align:-1px;margin-right:5px"><rect width="8" height="6" fill="#8cbb3c"/><path d="M0 0l4 3 4-3" stroke="#333" stroke-width=".8" fill="none"/></svg>info@k7pconsulting.com</span>
  <div class="abs foot-sep" style="left:306px"></div>

  <h4 class="abs foot-h" style="left:322px">Location Map</h4>
  <div class="abs foot-line" style="left:322px;width:131px"></div>
  <div class="abs map" role="img" aria-label="Street map showing the office location"></div>
  <div class="abs foot-sep" style="left:466px"></div>

  <div class="abs brand foot-brand" style="left:480px;top:1092px;font-size:8.4px"><span class="brand-dot" style="background:#999;width:10px;height:10px"></span>K7P Ledger &amp; Consulting</div>
  <span class="abs social" style="left:497px;background:#3b5a9a"></span>
  <span class="abs social" style="left:515px;background:#2aa3e0"></span>
  <span class="abs social" style="left:534px;background:#1a77b5"></span>
  <span class="abs social" style="left:552px;background:#e0442c"></span>

  <div class="abs copy">Copyright © 2017 K7Pconsulting . All Rights Reserved.</div>
</footer>

</body>
</html>
```